Rebrand of an existing product label

We are looking for a new design / label for our body lotion. Attached is the current product label. We have this product available in Retinol, Collagen, Hyaluronic Acid, Vitamin C, and Coconut. The brand should reflect a clinical, trustworthy look. We also want to include on the label that the product contains Dead Sea Minerals. Attached is the dieline for the label for the jar and the top. This jar is the packaging that needs to be used for this project.

Target Market(s)

40+

Requirements
Must have
• Ingredient callouts on the front + benefits. Ex- Vitamin C Brightening Cream

```html
<!DOCTYPE html>
<html lang="en">
<head>
<meta charset="UTF-8">
<title>Lumera Collagen Cream Label</title>
<link href="https://fonts.googleapis.com/css2?family=Jost:wght@400;500&family=Nunito:wght@800&family=Lexend:wght@400;600;700&display=swap" rel="stylesheet">
<style>
  :root {
    --bg: #ffffff;
    --ink: #1c1c1c;
    --navy: #2b2f7a;
    --purple-deep: #862a8f;
    --purple-mid: #a13fa8;
    --purple-soft: #b866bf;
    --pink-band: #f0d3f3;
    --pink-light: #fbf1fc;
    --lilac-shape: #e6b3ec;
    --white: #ffffff;
    --grey-rule: #d9d9d9;
    --drop-grey: #cfcfcf;
  }
  * { margin: 0; padding: 0; box-sizing: border-box; }
  html, body { width: 1200px; height: 927px; overflow: hidden; background: var(--bg); }
  .canvas { position: relative; width: 1200px; height: 927px; background: var(--bg); }

  /* Front jar label */
  .front-label {
    position: absolute; left: 70px; top: 250px; width: 680px; height: 420px;
    background: var(--white); overflow: hidden;
    border-top: 1px solid var(--grey-rule); border-bottom: 1px solid var(--grey-rule);
  }
  .front-label__band {
    position: absolute; left: 0; top: 0; width: 100%; height: 235px;
    background: radial-gradient(ellipse at 50% 55%, var(--pink-light) 0%, var(--pink-band) 75%);
  }
  .usage-badge {
    position: absolute; left: 22px; top: 40px; width: 90px; height: 90px;
    border-radius: 50%; background: var(--pink-light); border: 1px solid #e0b8e5;
    display: flex; align-items: center; justify-content: center; text-align: center;
    font-family: "Lexend", sans-serif; font-weight: 600; font-size: 11px;
    line-height: 1.3; letter-spacing: 0.5px; color: var(--navy);
  }
  .brand {
    position: absolute; left: 0; top: 100px; width: 100%;
    display: flex; justify-content: center; align-items: center; gap: 16px;
    font-family: "Jost", sans-serif; font-weight: 400; font-size: 56px;
    letter-spacing: 4px; color: var(--ink); line-height: 1;
  }
  .brand__dot { width: 18px; height: 18px; border-radius: 50%; background: var(--ink); }
  .size-note {
    position: absolute; left: 0; top: 176px; width: 100%; text-align: center;
    font-family: "Lexend", sans-serif; font-weight: 400; font-size: 17px;
    letter-spacing: 0.5px; color: var(--ink);
  }
  .product-pill {
    position: absolute; left: 118px; top: 212px; width: 470px; height: 92px;
    border-radius: 46px; border: 5px solid var(--white);
    background: linear-gradient(90deg, var(--purple-deep), var(--purple-soft));
    display: flex; align-items: center; justify-content: center;
    font-family: "Nunito", sans-serif; font-weight: 800; font-size: 78px;
    letter-spacing: 2px; color: var(--white);
  }
  .benefit-band {
    position: absolute; left: 110px; top: 305px; width: 540px; height: 38px;
    border-radius: 0 19px 19px 19px;
    background: linear-gradient(90deg, var(--purple-deep), var(--purple-soft));
    display: flex; align-items: center; justify-content: center;
    font-family: "Lexend", sans-serif; font-weight: 600; font-size: 17px;
    color: var(--white); letter-spacing: 0.6px;
  }
  .benefit-band__lead { font-weight: 400; margin-right: 6px; }
  .cream-drop {
    position: absolute; left: 40px; top: 250px; width: 52px; height: 76px;
    border-radius: 50% 50% 50% 50% / 62% 62% 38% 38%;
    background: radial-gradient(circle at 40% 65%, var(--white), var(--drop-grey));
  }
  .usage-line, .volume {
    position: absolute; top: 370px;
    font-family: "Lexend", sans-serif; font-weight: 400; font-size: 17px;
    color: var(--ink); letter-spacing: 0.6px;
  }
  .usage-line { left: 40px; }
  .volume { right: 40px; }

  /* Lid label */
  .lid-label {
    position: absolute; left: 810px; top: 280px; width: 360px; height: 360px;
    border-radius: 50%; background: var(--white); overflow: hidden;
    border: 1px solid var(--grey-rule);
  }
  .lid-label svg { position: absolute; left: 0; top: 0; }
  .lid-badge {
    position: absolute; left: 92px; top: 100px; width: 46px; height: 46px;
    border-radius: 50%; background: var(--pink-light); border: 1px solid #d9a6e0;
  }
  .lid-pill {
    position: absolute; left: 158px; top: 72px; width: 54px; height: 214px;
    writing-mode: vertical-rl; transform: rotate(180deg);
    border-radius: 27px; border: 3px solid var(--white);
    background: linear-gradient(0deg, var(--purple-deep), var(--purple-soft));
    display: flex; align-items: center; justify-content: center;
    font-family: "Nunito", sans-serif; font-weight: 800; font-size: 32px;
    letter-spacing: 1px; color: var(--white);
  }
  .lid-copy {
    position: absolute; left: 222px; top: 95px; height: 170px;
    writing-mode: vertical-rl; transform: rotate(180deg);
    display: flex; align-items: center; justify-content: center;
    font-family: "Lexend", sans-serif; font-weight: 600; font-size: 12px;
    line-height: 1.4; color: var(--ink); letter-spacing: 0.4px; text-align: center;
  }
</style>
</head>
<body>
<main class="canvas">

  <section class="front-label">
    <div class="front-label__band"></div>
    <p class="usage-badge">DEAD SEA<br>MINERALS</p>
    <div class="brand"><span>LUMERA</span><span class="brand__dot"></span></div>
    <p class="size-note">PROFESSIONAL SIZE</p>
    <div class="cream-drop" role="img" aria-label="Droplet of white cream"></div>
    <h1 class="product-pill">COLLAGEN</h1>
    <p class="benefit-band"><span class="benefit-band__lead">FOR</span>RADIANT, SOFT &amp; HEALTHIER LOOKING SKIN</p>
    <p class="usage-line">FOR FACE, NECK &amp; HANDS</p>
    <p class="volume">16.9 FL OZ (500 ML)</p>
  </section>

  <section class="lid-label">
    <svg width="360" height="360" viewBox="0 0 360 360" aria-hidden="true">
      <path d="M45 255 C70 220 135 235 148 180 C160 125 140 72 205 70 L360 70 L360 292 L85 292 C45 292 28 275 45 255 Z" fill="var(--lilac-shape)"/>
    </svg>
    <div class="lid-badge"></div>
    <div class="lid-pill">COLLAGEN</div>
    <p class="lid-copy">MOISTURIZING CREAM<br>FACE, NECK &amp; HANDS</p>
  </section>

</main>
</body>
</html>
```